Blind Rivet Product catalogue

Need a design in wordpress with a productcatalogue where i present all products. This is a B2B business. The products is Blindrivets and Blindrivet nuts and accessories to this. I only want the basic information and also technical specification.

This is a subcompany to my existing company k7.m9.se but specializing in a subcategory

Target Market(s)

Businesses using blind rivet technology.

Industry/Entity Type

Industrial

Coding

Coded - Design and coding required

Number of Pages Required

5+ page

Font styles to use
Sans Serif

Requirements
Must have
• Three different categories for the products; Blind Rivets - Blind Rivet Nut - Riveting Tools
Nice to have
• Possible to ad login for more information of the different sizes

```html
<!DOCTYPE html>
<html lang="en">
<head>
<meta charset="utf-8">
<title>K7M9 – Blind Rivet Product Catalogue</title>
<link rel="stylesheet" href="https://fonts.googleapis.com/css2?family=Orbitron:wght@700;900&family=Lato:wght@400;700;900&display=swap">
<style>
:root{
  --black:#000;
  --ink:#222;
  --muted:#666;
  --green:#5db33a;
  --red:#e3202b;
  --white:#fff;
  --line:#ddd;
  --faint:#f0f0f0;
}
*{margin:0;padding:0;box-sizing:border-box}
html,body{width:1200px;height:3656px;overflow:hidden}
body{position:relative;background:var(--white);font-family:'Lato',sans-serif;color:var(--ink)}
.abs{position:absolute}
.display{font-family:'Orbitron',sans-serif;font-weight:900;letter-spacing:1px}

/* header */
.site-header{left:0;top:0;width:1200px;height:95px;background:var(--black)}
.brand{display:flex;align-items:center;gap:8px;color:var(--white);font-weight:700;font-size:22px}
.brand-mark{width:14px;height:14px;background:var(--green)}
.search{left:636px;top:20px;width:186px;height:26px;background:#1b1b1b;border:1px solid #333;color:#888;font-size:11px;padding:6px 14px}
.search svg{position:absolute;right:8px;top:6px}
.btn-top{top:20px;height:26px;color:var(--white);font-size:11px;font-weight:700;text-align:center;line-height:26px}
.main-nav{left:316px;top:63px;display:flex;gap:15px;font-size:12px;font-weight:700;color:var(--white);white-space:nowrap}
.main-nav .active{position:relative}
.main-nav .active:after{content:"";position:absolute;left:-4px;right:-4px;top:23px;height:2px;background:var(--green)}

/* hero */
.hero{left:0;top:95px;width:1200px;height:640px}
.hero-title{left:143px;top:215px;font-size:92px;color:var(--white)}
.hero-sub{left:145px;top:340px;font-size:21px;line-height:30px;color:var(--white);font-weight:700}
.btn-slash{display:flex;align-items:center;justify-content:center;gap:6px;background:var(--green);color:var(--white);font-weight:700;font-size:17px;clip-path:polygon(6% 0,100% 0,94% 100%,0 100%)}
.btn-slash:before,.btn-slash:after{content:"";position:absolute;top:0;bottom:0;width:4px;background:var(--white);transform:skewX(20deg)}
.btn-slash:before{left:20px}.btn-slash:after{right:20px}
.dots{left:1113px;top:320px;display:flex;flex-direction:column;gap:11px}
.dots i{width:9px;height:9px;border-radius:50%;background:var(--white)}
.dots i.on{background:var(--green)}

/* category cards */
.cat{top:640px;width:298px;height:352px;background:var(--white);border:2px solid #e5e5e5;padding:10px;box-shadow:0 2px 4px rgba(0,0,0,.1)}
.cat-img{width:100%;height:282px;background:radial-gradient(circle at 50% 45%,#e9e9e9,#fff 70%)}
.cat-label{height:56px;color:var(--white);font-size:25px;font-weight:700;text-align:center;line-height:56px}

/* section headings */
.section-rule{left:582px;width:36px;height:4px;background:var(--green)}
.section-title{width:1200px;left:0;text-align:center;font-size:42px;color:var(--black)}
.welcome-text{left:195px;top:1208px;width:810px;text-align:center;font-size:14px;line-height:33.8px;color:var(--muted)}
.side-word{font-family:'Lato',sans-serif;font-weight:900;color:var(--faint);font-size:118px;letter-spacing:2px;transform-origin:left top;white-space:nowrap}

/* news grid */
.news-grid{left:0;top:1578px;width:1200px;height:636px;border-top:1px solid var(--line);border-bottom:1px solid var(--line);display:grid;grid-template-columns:400px 400px 400px;grid-template-rows:317px 317px}
.news-card{text-align:center;padding:52px 46px 0}
.news-date{color:var(--green);font-size:15px;display:flex;justify-content:center;gap:7px;align-items:center}
.news-title{margin-top:24px;font-size:18.5px;font-weight:400;text-transform:uppercase}
.news-text{margin-top:16px;font-size:12.6px;line-height:21.5px;color:var(--muted)}
.news-more{margin-top:22px;color:var(--red);font-weight:700;font-size:16px;display:flex;justify-content:center;gap:6px;align-items:center}
.photo{width:100%;height:100%}

/* contact */
.contact-item{width:300px;text-align:center;font-size:18px;line-height:26px;color:var(--ink)}
.field{border:1.5px solid #555;border-radius:22px;background:var(--white);font-size:12px;color:#555;padding:0 28px;line-height:40px}

/* footer */
.footer-col h3{font-size:16px;font-weight:700;color:var(--white);text-transform:uppercase}
.footer-col{color:var(--white);font-size:11px}
.quick li{list-style:none;margin-bottom:8.5px;padding-left:16px;position:relative}
.quick li:before{content:"";position:absolute;left:2px;top:3px;border-left:4px solid var(--white);border-top:3px solid transparent;border-bottom:3px solid transparent}
.info-row{display:flex;gap:12px;align-items:center;margin-top:14px}
.social{width:36px;height:36px;border:2px solid var(--white);border-radius:50%}
.copyright{left:0;top:3594px;width:1200px;text-align:center;color:var(--white);font-size:10.5px}
</style>
</head>
<body>

<!-- header -->
<header class="abs site-header">
  <div class="abs brand" style="left:145px;top:30px"><span class="brand-mark"></span>K7M9</div>
  <div class="abs search">Search
    <svg width="12" height="12" viewBox="0 0 12 12"><circle cx="5" cy="5" r="3.6" fill="none" stroke="#fff" stroke-width="1.6"/><line x1="7.6" y1="7.6" x2="11" y2="11" stroke="#fff" stroke-width="1.8"/></svg>
  </div>
  <div class="abs btn-top" style="left:832px;width:106px;background:var(--green)">INLOGGNING</div>
  <div class="abs btn-top" style="left:948px;width:107px;background:var(--red)">REGISTER</div>
  <nav class="abs main-nav">
    <span class="active">MARIN</span><span>SCREW</span><span>STICKS</span><span>NUTS</span><span>TRAYS</span><span>SCREW PIN</span><span>OTHER ATTACHMENT</span><span>CONTACT US</span><span>ABOUT US</span><span>SITEMAP</span>
  </nav>
</header>

<!-- hero -->
<svg class="abs hero" viewBox="0 0 1200 640" role="img" aria-label="Photo of a gloved hand using a pneumatic riveting tool on a metal workpiece">
  <defs>
    <linearGradient id="heroBg" x1="0" y1="0" x2="1" y2="1">
      <stop offset="0" stop-color="#2a2522"/><stop offset=".55" stop-color="#4a3f38"/><stop offset="1" stop-color="#1c1815"/>
    </linearGradient>
  </defs>
  <polygon points="0,0 1200,0 1200,585 600,640 0,585" fill="url(#heroBg)"/>
  <polyline points="0,588 600,643 1200,588" fill="none" stroke="#e3202b" stroke-width="3"/>
  <polyline points="0,593 600,648 1200,593" fill="none" stroke="#5db33a" stroke-width="3"/>
</svg>
<div class="abs display hero-title">K7M9</div>
<div class="abs hero-sub">Lorem ipsum dolor sit amet, consectetur<br>adipiscing elit&nbsp; sed do eiusmod</div>
<div class="abs btn-slash" style="left:145px;top:446px;width:232px;height:52px">GET STARTED <svg width="14" height="14" viewBox="0 0 14 14"><circle cx="7" cy="7" r="7" fill="#fff"/><path d="M5.5 4 8.5 7 5.5 10" stroke="#5db33a" stroke-width="2" fill="none"/></svg></div>
<div class="abs dots"><i></i><i></i><i class="on"></i><i></i><i></i></div>

<!-- categories -->
<div class="abs cat" style="left:130px">
  <div class="cat-img" role="img" aria-label="Product photo of a blind rivet"></div>
  <div class="cat-label" style="background:var(--green)">Blind Rivets</div>
</div>
<div class="abs cat" style="left:450px">
  <div class="cat-img" role="img" aria-label="Product photo of a blind rivet nut"></div>
  <div class="cat-label" style="background:var(--red)">Blind Rivet Nut</div>
</div>
<div class="abs cat" style="left:770px">
  <div class="cat-img" role="img" aria-label="Product photo of a cordless riveting tool"></div>
  <div class="cat-label" style="background:var(--green)">Riveting Tools</div>
</div>

<!-- welcome -->
<div class="abs side-word" style="left:1085px;top:1545px;transform:rotate(-90deg)">WELCOME</div>
<div class="abs section-rule" style="top:1092px"></div>
<h1 class="abs display section-title" style="top:1124px">WELCOME TO K7M9</h1>
<p class="abs welcome-text">K7M9 sells stainless steel fasteners to stores, retailers and industry. On our site you can find most known DIN and ISO standards in mounting. We also have a large range of Marine products in stainless steel. Welcome to look around our store. You navigate through the menu at the top of the page, if you want to see an overview of all products in a certain category, click on the name. For example, if you move your mouse over screws in the menu and click on wooden screws, all products in that category are displayed. Each item has a packaging size that is also the smallest order item!</p>
<div class="abs btn-slash" style="left:484px;top:1422px;width:232px;height:53px">READ MORE <svg width="14" height="14" viewBox="0 0 14 14"><circle cx="7" cy="7" r="7" fill="#fff"/><path d="M5.5 4 8.5 7 5.5 10" stroke="#5db33a" stroke-width="2" fill="none"/></svg></div>

<!-- news -->
<section class="abs news-grid">
  <article class="news-card">
    <div class="news-date"><svg width="14" height="13" viewBox="0 0 14 13"><rect x="1" y="2" width="12" height="10" fill="none" stroke="#5db33a" stroke-width="1.5"/><line x1="1" y1="5" x2="13" y2="5" stroke="#5db33a" stroke-width="1.5"/></svg>APRIL 09,2020</div>
    <h2 class="news-title">Lorem ipsum dolor sit amet</h2>
    <p class="news-text">Lorem ipsum dolor sit amet, consectetur adipiscing elit, sed do eiusmod tempor incididunt ut labore et dolore magna aliquaenim ad minimquis nostrud exercitation ullamco veniam</p>
    <div class="news-more">READ MORE <svg width="13" height="13" viewBox="0 0 14 14"><circle cx="7" cy="7" r="7" fill="#e3202b"/><path d="M5.5 4 8.5 7 5.5 10" stroke="#fff" stroke-width="2" fill="none"/></svg></div>
  </article>
  <div class="photo" role="img" aria-label="Photo of a worker riveting a metal part with a hand tool" style="background:linear-gradient(135deg,#4a5560,#2b2622 55%,#6a5a48)"></div>
  <article class="news-card">
    <div class="news-date"><svg width="14" height="13" viewBox="0 0 14 13"><rect x="1" y="2" width="12" height="10" fill="none" stroke="#5db33a" stroke-width="1.5"/><line x1="1" y1="5" x2="13" y2="5" stroke="#5db33a" stroke-width="1.5"/></svg>APRIL 09,2020</div>
    <h2 class="news-title">Lorem ipsum dolor sit amet</h2>
    <p class="news-text">Lorem ipsum dolor sit amet, consectetur adipiscing elit, sed do eiusmod tempor incididunt ut labore et dolore magna aliquaenim ad minimquis nostrud exercitation ullamco veniam</p>
    <div class="news-more">READ MORE <svg width="13" height="13" viewBox="0 0 14 14"><circle cx="7" cy="7" r="7" fill="#e3202b"/><path d="M5.5 4 8.5 7 5.5 10" stroke="#fff" stroke-width="2" fill="none"/></svg></div>
  </article>
  <div class="photo" role="img" aria-label="Photo of a hand riveter in an open case of assorted rivets on a wooden table" style="background:linear-gradient(135deg,#8a6a55,#2a2a2a 50%,#b5a03a 75%,#7a5a45)"></div>
  <article class="news-card">
    <div class="news-date"><svg width="14" height="13" viewBox="0 0 14 13"><rect x="1" y="2" width="12" height="10" fill="none" stroke="#5db33a" stroke-width="1.5"/><line x1="1" y1="5" x2="13" y2="5" stroke="#5db33a" stroke-width="1.5"/></svg>APRIL 09,2020</div>
    <h2 class="news-title">Lorem ipsum dolor sit amet</h2>
    <p class="news-text">Lorem ipsum dolor sit amet, consectetur adipiscing elit, sed do eiusmod tempor incididunt ut labore et dolore magna aliquaenim ad minimquis nostrud exercitation ullamco veniam</p>
    <div class="news-more">READ MORE <svg width="13" height="13" viewBox="0 0 14 14"><circle cx="7" cy="7" r="7" fill="#e3202b"/><path d="M5.5 4 8.5 7 5.5 10" stroke="#fff" stroke-width="2" fill="none"/></svg></div>
  </article>
  <div class="photo" role="img" aria-label="Photo of a worker in blue overalls using a riveting tool" style="background:linear-gradient(135deg,#1a3aa0,#2f5fd0 50%,#8aa0b8)"></div>
</section>

<!-- contact -->
<div class="abs side-word" style="left:60px;top:2930px;transform:rotate(-90deg)">CONTACT</div>
<div class="abs section-rule" style="top:2344px"></div>
<h2 class="abs display section-title" style="top:2378px">GET IN TOUCH</h2>

<svg class="abs" style="left:0;top:2490px" width="1200" height="140" viewBox="0 0 1200 140">
  <line x1="310" y1="65" x2="510" y2="65" stroke="#bbb" stroke-width="1.5" stroke-dasharray="2 4"/>
  <line x1="620" y1="65" x2="860" y2="65" stroke="#bbb" stroke-width="1.5" stroke-dasharray="2 4"/>
  <g>
    <path d="M254 125 L236 110 A54 54 0 1 1 272 110 Z" fill="#fff" stroke="#5db33a" stroke-width="3"/>
    <circle cx="254" cy="65" r="44" fill="#5db33a"/>
    <path d="M240 50 q-4 6 2 16 q8 14 20 18 q6 2 10-3 l-7-7 q-4 3-7 0 l-8-9 q-2-3 1-6 z" fill="#fff"/>
  </g>
  <g>
    <path d="M565 125 L547 110 A54 54 0 1 1 583 110 Z" fill="#fff" stroke="#e3202b" stroke-width="3"/>
    <circle cx="565" cy="65" r="44" fill="#e3202b"/>
    <path d="M548 67 L565 51 L582 67 M553 63 V80 H561 V70 H569 V80 H577 V63" fill="#fff" stroke="#fff" stroke-width="3" stroke-linejoin="round"/>
  </g>
  <g>
    <path d="M916 125 L898 110 A54 54 0 1 1 934 110 Z" fill="#fff" stroke="#5db33a" stroke-width="3"/>
    <circle cx="916" cy="65" r="44" fill="#5db33a"/>
    <rect x="895" y="51" width="42" height="30" rx="3" fill="#fff"/>
    <path d="M895 54 L916 70 L937 54" fill="none" stroke="#5db33a" stroke-width="3"/>
  </g>
</svg>
<div class="abs contact-item" style="left:104px;top:2637px">Phone<br>0300-12 34 56</div>
<div class="abs contact-item" style="left:415px;top:2637px">345,ed ut perspiciatis unde omnis<br>iste natus erro</div>
<div class="abs contact-item" style="left:766px;top:2637px">Email<br>info@k7m9-rivets.se</div>

<form>
  <div class="abs field" style="left:218px;top:2773px;width:372px;height:42px">Enter Name</div>
  <div class="abs field" style="left:609px;top:2773px;width:372px;height:42px">Enter Email</div>
  <div class="abs field" style="left:218px;top:2833px;width:372px;height:42px">Phone</div>
  <div class="abs field" style="left:609px;top:2833px;width:372px;height:42px">Address</div>
  <div class="abs field" style="left:218px;top:2893px;width:763px;height:75px;border-radius:24px;line-height:36px">Message</div>
</form>
<div class="abs btn-slash" style="left:468px;top:3022px;width:264px;height:54px">SUBMIT MESSAGE <svg width="14" height="14" viewBox="0 0 14 14"><circle cx="7" cy="7" r="7" fill="#fff"/><path d="M5.5 4 8.5 7 5.5 10" stroke="#5db33a" stroke-width="2" fill="none"/></svg></div>

<!-- footer -->
<svg class="abs" style="left:0;top:3160px" width="1200" height="496" viewBox="0 0 1200 496">
  <polygon points="0,196 600,14 1200,196 1200,496 0,496" fill="#000"/>
  <polyline points="0,190 600,6 1200,190" fill="none" stroke="#e3202b" stroke-width="5"/>
  <polyline points="0,196 600,14 1200,196" fill="none" stroke="#5db33a" stroke-width="4"/>
</svg>
<div class="abs brand" style="left:145px;top:3378px;font-size:24px"><span class="brand-mark"></span>K7M9</div>
<div class="abs" style="left:143px;top:3450px;display:flex;gap:9px" aria-label="Social links">
  <span class="social"></span><span class="social"></span><span class="social"></span><span class="social"></span>
</div>

<div class="abs footer-col" style="left:380px;top:3345px;width:230px">
  <h3>Contact Us</h3>
  <p style="margin-top:16px;line-height:18px">345,ed ut perspiciatis unde omnis iste natus erro</p>
  <div class="info-row"><svg width="16" height="16" viewBox="0 0 16 16"><path d="M3 1 q-3 4 1 9 q4 5 9 5 l2-3-3-2-2 1-4-4 1-2-2-3z" fill="none" stroke="#fff" stroke-width="1.2"/></svg>Phone: 0300-12 34 56</div>
  <div class="info-row"><svg width="16" height="16" viewBox="0 0 16 16"><circle cx="8" cy="8" r="7" fill="none" stroke="#fff" stroke-width="2"/><circle cx="8" cy="8" r="2.5" fill="#fff"/></svg>Mon – Fri: 9AM – 5.30PM</div>
  <div class="info-row"><svg width="16" height="12" viewBox="0 0 16 12"><rect x="1" y="1" width="14" height="10" fill="none" stroke="#fff"/><path d="M1 1 L8 7 L15 1" fill="none" stroke="#fff"/></svg>info@k7m9-rivets.se</div>
</div>

<div class="abs footer-col" style="left:648px;top:3345px;width:160px">
  <h3>Quick Links</h3>
  <ul class="quick" style="margin-top:18px">
    <li>Marin</li><li>Screw</li><li>Sticks</li><li>Nuts</li><li>Trays</li><li>Screw Pin</li><li>Other attachment</li>
  </ul>
</div>

<div class="abs footer-col" style="left:843px;top:3345px;width:220px">
  <h3>Sign up for Newsletter</h3>
  <p style="margin-top:14px;line-height:16px;font-size:10.5px">Excepteur sint occaecat cupidatat non proident, sunt in culpa qui</p>
  <div style="margin-top:14px;width:212px;height:38px;background:#fff;color:#555;font-size:10.5px;padding:0 14px;line-height:38px">Enter Name</div>
  <div style="margin-top:18px;width:95px;height:37px;background:var(--green);color:#fff;font-size:12px;text-align:center;line-height:37px">SUBSCRIBE</div>
</div>

<div class="abs copyright">2020 © Copyrights K7M9 . All Rights Reserved &nbsp;|&nbsp; Privacy Policy &nbsp;|&nbsp; Contact Us &nbsp;|&nbsp; About us &nbsp;|&nbsp; Sitemap</div>

</body>
</html>
```